Flyer PRTW

Everyone deserves true happiness.
Real Food is the answer to:
A body you love
Reverting illnesses
Healthy digestion
Stable blood sugar
Emotions in control
Blasting energy
Sound sleep
REAL food + water + exercise + Laughter =
“HIGH QUALITY OF LIFE “
EASY, right?
Challenging: certainly
Changing habits: reluctance in sight!
WE’RE OFFER TO:
1. Study YOUR unique body composition, food cravings, blockages, illnesses, and personality!
2. Introduce you to new Food
3. customized wellness plan with follow ups
4. meditation,cooking, and fitness classes as well as wellness workshops
5. New friends with high aspirations
LOGO
Contact info
Please visit our web address to see our design style and colors: www.pinerivertallwave.net
Target Market(s)
people who want to be more healthy
Industry/Entity Type
Fitness
Requirements
Must have
- beautiful pictures of fresh food (main picture) and maybe a few more small pictures reflecting
exercise
healthy living
meditation
Nice to have
- look is crucial. recall some of the color or colors from my logo to have a theme

```html
<!DOCTYPE html>
<html lang="en">
<head>
<meta charset="utf-8">
<title>PRTW Flyer</title>
<link href="https://fonts.googleapis.com/css2?family=Ubuntu:ital,wght@0,400;0,500;0,700;1,400;1,500;1,700&display=swap" rel="stylesheet">
<style>
  :root {
    --frame-orange: #e8921f;
    --field-green: #0e8538;
    --ink: #1f2a22;
    --brand-lime: #8cc63f;
    --accent-orange: #f39a1e;
    --food-red: #d9482b;
    --food-leaf: #5fae3a;
    --food-yellow: #f2c23a;
  }
  html, body {
    margin: 0;
    padding: 0;
    overflow: hidden;
  }
  .flyer {
    position: relative;
    width: 900px;
    height: 1200px;
    box-sizing: border-box;
    background: var(--field-green);
    border: 16px solid var(--frame-orange);
    font-family: "Ubuntu", Verdana, sans-serif;
    color: var(--ink);
    overflow: hidden;
  }
  .headline {
    position: absolute;
    top: 134px;
    left: 0;
    right: 0;
    margin: 0;
    text-align: center;
    font-size: 32px;
    font-weight: 700;
    font-style: italic;
    line-height: 43px;
  }
  .headline .gap {
    display: block;
    height: 43px;
  }
  .food-photo {
    position: absolute;
    top: 340px;
    left: 60px;
    right: 60px;
    height: 168px;
    border-radius: 10px;
    background: linear-gradient(110deg, var(--food-red) 0%, var(--food-yellow) 35%, var(--food-leaf) 70%, var(--brand-lime) 100%);
  }
  .offer {
    position: absolute;
    top: 520px;
    left: 40px;
    right: 40px;
    font-size: 22px;
    font-style: italic;
    line-height: 29.5px;
  }
  .offer-title {
    margin: 0;
    text-align: center;
    font-weight: 400;
    font-size: 22px;
  }
  .offer-list {
    list-style: none;
    margin: 0;
    padding: 0;
  }
  .offer-item {
    position: relative;
    text-align: center;
    padding: 0 44px 0 56px;
  }
  .offer-num {
    position: absolute;
    left: 22px;
    top: 0;
  }
  .benefits {
    position: absolute;
    top: 758px;
    left: 60px;
    right: 60px;
    text-align: center;
    font-size: 18px;
    font-style: italic;
    line-height: 24px;
  }
  .benefits-lead {
    margin: 0 0 4px;
    font-weight: 700;
  }
  .benefits-list {
    list-style: none;
    margin: 0 auto;
    padding: 0;
    width: 520px;
    columns: 2;
    text-align: left;
  }
  .benefits-list li::before {
    content: "•";
    color: var(--accent-orange);
    margin-right: 8px;
  }
  .formula {
    margin: 6px 0 0;
    font-weight: 700;
  }
  .brand {
    position: absolute;
    left: 10px;
    bottom: 20px;
    display: flex;
    align-items: center;
    gap: 24px;
  }
  .brand-mark {
    width: 180px;
    height: 180px;
  }
  .brand-name {
    font-size: 88px;
    font-weight: 400;
    color: #111;
    letter-spacing: 2px;
  }
  .site {
    position: absolute;
    right: 10px;
    bottom: 4px;
    margin: 0;
    font-size: 23px;
    font-weight: 700;
    font-style: italic;
    color: #111;
  }
  .site .hl {
    color: var(--accent-orange);
  }
</style>
</head>
<body>
  <main class="flyer">
    <h1 class="headline">
      EASY, right?<br>
      Challenging: certainly
      <span class="gap"></span>
      Changing habits: reluctance in sight!
    </h1>

    <div class="food-photo" role="img" aria-label="Photograph of fresh fruit and vegetables"></div>

    <section class="offer">
      <h2 class="offer-title">WE’RE HERE TO:</h2>
      <ol class="offer-list">
        <li class="offer-item"><span class="offer-num">1.</span>Study YOUR unique body composition, food cravings, blockages, illnesses, and personality!</li>
        <li class="offer-item"><span class="offer-num">2.</span>Educate – guide – develop plan – and follow you up 24/7</li>
        <li class="offer-item"><span class="offer-num">3.</span>You will: taste new food, plan meals, groceries shopping.</li>
        <li class="offer-item"><span class="offer-num">4.</span>You’ll attend: meditation, cooking, and fitness classes</li>
        <li class="offer-item"><span class="offer-num">5.</span>You’ll make new friends</li>
      </ol>
    </section>

    <section class="benefits">
      <p class="benefits-lead">Everyone deserves true happiness. Real Food is the answer to:</p>
      <ul class="benefits-list">
        <li>A body you love</li>
        <li>Reverting illnesses</li>
        <li>Healthy digestion</li>
        <li>Stable blood sugar</li>
        <li>Emotions in control</li>
        <li>Blasting energy</li>
        <li>Sound sleep</li>
      </ul>
      <p class="formula">REAL food + water + exercise + Laughter = “HIGH QUALITY OF LIFE”</p>
    </section>

    <div class="brand">
      <svg class="brand-mark" viewBox="0 0 180 180" aria-hidden="true">
        <circle cx="90" cy="90" r="84" fill="var(--brand-lime)"/>
      </svg>
      <span class="brand-name">PRTW</span>
    </div>

    <p class="site">www.pineriver<span class="hl">tallwave</span>.net</p>
  </main>
</body>
</html>
```